Award-winnning Estate Agent needs a premium version of their 'For Sale' board design

We need a premium option for our 'For Sale' board design. We have a standard board that is attached to this brief, but were are looking to have a premium design version that we will use when selling exclusive properties. Our company name is Harbour Lane Estates and the name for this is exclusive selection is: 'The Harbour Collection'. The design needs to work with our current brand, but have a distinctive PREMIUM feel to it. I have uploaded the barnd guidelines and also some of the exisisting logo variations. We do NOT need a new logo but feel free to play around with colours, fonts, sizes etc. for the sign.

Target Market(s)

Property buyers & house hunters

Industry/Entity Type

Real Estate - Residential Property

Font styles to use
Sans Serif

Requirements
Must have
• A premium fee, must be square design, must be easy to read when driving past the sign
Nice to have
• I'm open ot ideas

```html
<!DOCTYPE html>
<html lang="en">
<head>
<meta charset="utf-8">
<title>Harbour Lane Estates – For Sale Board</title>
<link href="https://fonts.googleapis.com/css2?family=Arimo:wght@400;600;700&family=Montserrat:wght@600;700;800&display=swap" rel="stylesheet">
<style>
  :root {
    --navy: #0d1160;
    --white: #ffffff;
    --cream: #fffdf4;
    --brand-purple: #3d2c7e;
    --brand-blue: #4a6aa8;
    --gold-dark: #b08a3a;
    --gold-mid: #c9a24c;
    --gold-light: #f4e3a6;
    --page: #ffffff;
  }
  html, body {
    margin: 0;
    padding: 0;
    width: 1200px;
    height: 1000px;
    overflow: hidden;
    background: var(--page);
  }
  .canvas {
    position: relative;
    width: 1200px;
    height: 1000px;
  }
  .sale-board {
    position: absolute;
    left: 280px;
    top: 180px;
    width: 640px;
    height: 640px;
  }
  .board-frame-edge { fill: var(--gold-mid); }
  .board-frame { fill: var(--navy); }
  .board-panel { fill: var(--white); }
  .corner-navy { fill: var(--navy); }
  .brand-mark { fill: var(--brand-blue); }
  .collection-name {
    font-family: "Montserrat", Arial, sans-serif;
    font-weight: 600;
    letter-spacing: 3px;
    fill: var(--gold-dark);
  }
  .brand-name {
    font-family: "Arimo", Arial, sans-serif;
    font-weight: 600;
    fill: var(--brand-purple);
  }
  .sale-title {
    font-family: "Montserrat", Arial, sans-serif;
    font-weight: 800;
    fill: var(--cream);
  }
  .phone-number {
    font-family: "Montserrat", Arial, sans-serif;
    font-weight: 800;
    fill: var(--navy);
  }
  .web-address {
    font-family: "Arimo", Arial, sans-serif;
    font-weight: 700;
    fill: var(--white);
  }
</style>
</head>
<body>
<main class="canvas">
  <svg class="sale-board" viewBox="0 0 640 640" role="img" aria-label="Harbour Lane Estates, The Harbour Collection, For Sale board">
    <defs>
      <linearGradient id="gold" x1="0" y1="0" x2="1" y2="0">
        <stop offset="0" stop-color="var(--gold-dark)"/>
        <stop offset="0.25" stop-color="var(--gold-light)"/>
        <stop offset="0.5" stop-color="var(--gold-mid)"/>
        <stop offset="0.75" stop-color="var(--gold-light)"/>
        <stop offset="1" stop-color="var(--gold-dark)"/>
      </linearGradient>
    </defs>

    <rect class="board-frame-edge" x="0" y="0" width="640" height="640"/>
    <rect class="board-frame" x="4" y="4" width="632" height="632"/>
    <rect class="board-panel" x="18" y="18" width="604" height="604"/>

    <polygon class="corner-navy" points="18,18 82,18 18,122"/>
    <polygon fill="url(#gold)" points="18,150 18,122 82,18 104,18"/>
    <polygon class="corner-navy" points="622,18 558,18 622,122"/>
    <polygon fill="url(#gold)" points="622,150 622,122 558,18 536,18"/>

    <rect class="brand-mark" x="282" y="40" width="76" height="76"/>
    <text class="collection-name" x="320" y="160" font-size="22" text-anchor="middle">THE HARBOUR COLLECTION</text>
    <text class="brand-name" x="320" y="228" font-size="42" text-anchor="middle" textLength="480" lengthAdjust="spacingAndGlyphs">Harbour Lane Estates</text>

    <polygon fill="url(#gold)" points="0,302 22,254 618,254 640,302 618,350 22,350" transform="translate(0,50)"/>
    <text class="sale-title" x="320" y="393" font-size="92" text-anchor="middle" textLength="540" lengthAdjust="spacingAndGlyphs">FOR SALE</text>

    <text class="phone-number" x="320" y="520" font-size="74" text-anchor="middle" textLength="540" lengthAdjust="spacingAndGlyphs">01632 960418</text>

    <polygon fill="url(#gold)" points="100,557 540,557 622,622 18,622"/>
    <polygon class="board-frame" points="112,566 528,566 600,622 40,622"/>
    <text class="web-address" x="320" y="604" font-size="24" text-anchor="middle" textLength="440" lengthAdjust="spacingAndGlyphs">www.harbourlaneestates.co.uk</text>
  </svg>
</main>
</body>
</html>
```